THE NAME OF THE COMPANY IS: MEADOW CRAFTWORKS. Services including: Excavation , Custom Property Designs, Sustainable Vegetable Gardens, Beautiful Floriculture. Licensed Contractor with 35 years experience. I am looking for 4 simple Icons: One a tractor, signifying the Excavation work, one a pencil and paper or ruler or something to signify Custom Designs, one a vegetable and one a flower. Similar Icons to the Hollow Fern Logos (attached). The Icons will all be simple but easily identifiable. All of them should look in the same style. I am thinking about a color screen of various olive toned greens. See PMS color chart attached.Probably a white reverse in green tone squares. I'd be interested in different layouts of a business card which will translate to signs and truck door magnets for a full sized truck. It'd also need it to translate to stationary and give away items.

Target Market(s)

The target market is a homeowner with disposable inclome to afford a high end Landscape Artist.

Industry/Entity Type

Business

Contact Information for Business Card

Meadow Craftworks
Excavation, Custom Designs, Sustainable Gardens, Floriculture
Dwight Kessler
Contractor
Ca. Lic. # C27-590418
PO Box 274916 Carlsbad, Ca 92047
760-829-1647

Colors
acd036
33b7a4

Requirements
Must have
• The company name MEADOW CRAFTWORKS needs to be prominent with the tag line: Excavation, Custom Property Designs, Sustainable Gardens and Floraculture being centered underneath the name. Be creative with the card color and use different shades of the greens I provided for the icons.

```html
<!DOCTYPE html>
<html lang="en">
<head>
<meta charset="utf-8">
<title>Meadow Craftworks — Business Card</title>
<link href="https://fonts.googleapis.com/css2?family=Dosis:wght@300;400&family=Oswald:wght@500&display=swap" rel="stylesheet">
<style>
  :root {
    --backdrop: #2a2d33;
    --card-rim: #6a7a34;
    --card-rim-light: #8a9a4c;
    --card-face: #f3f4f1;
    --olive: #7f8c3f;
    --olive-deep: #5d6b2a;
    --mauve: #d9c6c6;
    --artwork-light: #ffffff;
  }
  html, body {
    margin: 0;
    width: 1200px;
    height: 900px;
    overflow: hidden;
    background: var(--backdrop);
  }
  .canvas {
    width: 1200px;
    height: 900px;
    display: flex;
    align-items: center;
    justify-content: center;
  }
  .business-card {
    width: 900px;
    height: 520px;
    box-sizing: border-box;
    padding: 14px;
    border-radius: 40px;
    background: linear-gradient(135deg, var(--card-rim-light), var(--card-rim));
  }
  .card-face {
    width: 100%;
    height: 100%;
    border-radius: 28px;
    background: var(--card-face);
    display: flex;
    flex-direction: column;
    align-items: center;
    padding-top: 40px;
    box-sizing: border-box;
  }
  .brand-artwork {
    width: 430px;
    height: 220px;
    border-radius: 14px;
    background: linear-gradient(90deg, var(--artwork-light) 0%, var(--mauve) 45%, var(--artwork-light) 70%, var(--mauve) 100%);
    opacity: 0.85;
  }
  .company-name {
    margin: 16px 0 0;
    font-family: "Dosis", sans-serif;
    font-weight: 300;
    font-size: 60px;
    letter-spacing: 4px;
    line-height: 1;
    color: var(--olive);
    white-space: nowrap;
  }
  .services {
    margin: 10px 0 0;
    font-family: "Dosis", sans-serif;
    font-weight: 400;
    font-size: 14px;
    letter-spacing: 1px;
    line-height: 1;
    text-transform: uppercase;
    color: var(--olive);
    white-space: nowrap;
  }
  .services .dot { margin: 0 3px; }
  .contact-line {
    margin: 22px 0 0;
    font-family: "Oswald", sans-serif;
    font-weight: 500;
    font-size: 22px;
    letter-spacing: 2.5px;
    line-height: 1;
    text-transform: uppercase;
    color: var(--olive-deep);
    white-space: nowrap;
  }
</style>
</head>
<body>
  <main class="canvas">
    <section class="business-card">
      <div class="card-face">
        <div class="brand-artwork" role="img" aria-label="Brand artwork area in white and soft mauve"></div>
        <h1 class="company-name">MEADOW CRAFTWORKS</h1>
        <p class="services">Excavation<span class="dot">•</span>Custom Property Designs<span class="dot">•</span>Sustainable Gardens<span class="dot">•</span>Floraculture</p>
        <p class="contact-line">Dwight Kessler Contractor Ca. Lic. # PO Box Carlsbad, Ca 760-</p>
      </div>
    </section>
  </main>
</body>
</html>
```